Tavrelo.com.au - AV and Communications Installation Company Website

A company website for a modern, high level/enterprise communications installation/engineering company based in Sydney Australia.
My client base is construction companies working in medical, government and educations departments so the website needs to look professional.
Clients like Quenby or Dorvik as I want to eventually move into data centre design and installation so I need something appealing to the high end market.
Fiber Optic Installation is a massive part of the company aswell.
Audio visual, IT installation is also what the company will be involved in.
I want the website to be modern, eye catching, professional looking.

Target Market(s)

High end clients and construction companies

Industry/Entity Type

Communications

Coding

Coded - Design and coding required

Number of Pages Required

1 page

Requirements
Must have
• Modern and clean layout with links to other social media platforms

```html
<!DOCTYPE html>
<html lang="en">
<head>
<meta charset="utf-8">
<title>Tavrelo — Communications Installation</title>
<link rel="stylesheet" href="https://fonts.googleapis.com/css2?family=Outfit:wght@300;400;500&family=Poppins:wght@400;500;600&display=swap">
<style>
:root{
  --teal:#1a8f9f;
  --teal-dark:#137583;
  --ink:#1d1d1d;
  --grey:#6b6d72;
  --muted:#777;
  --field:#e3e6e8;
  --black:#000;
  --white:#fff;
}
*{box-sizing:border-box;margin:0;padding:0}
html,body{width:1200px;height:3276px;overflow:hidden}
body{position:relative;background:var(--white);font-family:"Poppins",sans-serif;color:var(--ink)}
.abs{position:absolute}
.heading{font-family:"Outfit",sans-serif;font-weight:400;color:var(--ink)}

/* header */
.site-header{position:absolute;left:0;top:0;width:1200px;height:80px;background:#f6f6f6}
.brand{position:absolute;left:85px;top:20px;font-family:"Outfit",sans-serif;font-size:40px;font-weight:400;color:var(--teal);letter-spacing:1px;line-height:40px}
.nav a{position:absolute;top:31px;font-family:"Outfit",sans-serif;font-size:15px;color:#222;text-decoration:none}
.nav a.active{color:var(--teal)}
.social{position:absolute;width:32px;height:32px;border-radius:50%;background:var(--grey)}
.social.on{background:var(--teal)}
.pill{position:absolute;border-radius:20px;font-size:11px;font-weight:500;letter-spacing:.5px;text-align:center;text-decoration:none}
.pill.solid{background:var(--teal);color:var(--white)}
.pill.outline{border:1.5px solid var(--teal);color:var(--teal);background:var(--white)}

/* hero */
.hero-photo{position:absolute;left:0;top:80px;width:1200px;height:602px;
  background:linear-gradient(100deg,#5d4a38 0%,#7b6450 35%,#8c7a66 60%,#5a4a3c 100%)}
.hero-title{position:absolute;left:85px;top:206px;font-family:"Outfit",sans-serif;font-size:47px;font-weight:400;color:var(--white)}
.hero-sub{position:absolute;left:85px;top:276px;font-family:"Outfit",sans-serif;font-size:18.5px;line-height:23px;color:var(--white)}
.hero-btn{position:absolute;left:85px;top:358px;width:129px;height:31px;border:1.5px solid var(--white);border-radius:16px;color:var(--white);font-size:10.5px;font-weight:500;text-align:center;line-height:28px}
.dot{position:absolute;left:1101px;width:14px;height:14px;border:1.2px solid var(--white);border-radius:50%}
.dot.on::after{content:"";position:absolute;left:3px;top:3px;width:6px;height:6px;border-radius:50%;background:var(--white)}

/* section titles */
.eyebrow{position:absolute;left:0;width:1200px;text-align:center;font-size:12px;font-weight:600;letter-spacing:.6px;color:var(--teal)}
.eyebrow span{display:inline-block;position:relative}
.eyebrow span::before,.eyebrow span::after{content:"";position:absolute;top:50%;width:48px;height:1px;background:var(--teal)}
.eyebrow span::before{right:calc(100% + 18px)}
.eyebrow span::after{left:calc(100% + 18px)}
.section-title{position:absolute;left:0;width:1200px;text-align:center;font-size:38px}

/* services */
.service{position:absolute;top:733px;width:246px;height:322px;display:flex;flex-direction:column;align-items:center;justify-content:flex-start;padding-top:178px;color:var(--white);font-size:15px;font-weight:600;text-align:center;line-height:19px}
.service.fiber{left:85px;background:linear-gradient(160deg,#3a6fa8,#1e4f86 55%,#2b6aa0)}
.service.av{left:346px;padding-top:114px;background:linear-gradient(160deg,#2ba0ae,#1a8f9f)}
.service.comms{left:608px;background:linear-gradient(160deg,#6b7d8e,#4e5660 60%,#8f9296)}
.service.security{left:869px;background:linear-gradient(160deg,#b8a58a,#8e7f6c 55%,#6f6a63)}
.service.av .frame{position:absolute;left:17px;top:17px;right:17px;bottom:17px;border:1.5px solid var(--white)}
.service svg{margin-bottom:14px}

/* about */
.about-mark{position:absolute;left:85px;top:1152px;width:481px;height:305px;display:flex;align-items:center;justify-content:center;gap:20px}
.about-mark .sq{width:90px;height:90px;background:var(--teal)}
.about-mark .name{font-family:"Outfit",sans-serif;font-size:82px;font-weight:400;color:var(--teal)}
.eyebrow-left{position:absolute;left:616px;top:1147px;font-size:12px;font-weight:600;letter-spacing:.6px;color:var(--teal)}
.eyebrow-left::after{content:"";position:absolute;left:calc(100% + 18px);top:50%;width:48px;height:1px;background:var(--teal)}
.about-title{position:absolute;left:616px;top:1168px;font-size:38px}
.about-text{position:absolute;left:616px;top:1240px;width:500px;font-size:11.6px;line-height:19.4px;color:var(--muted)}
.about-text p+p{margin-top:19px}

/* projects */
.tile{position:absolute;width:338px;height:201px}
.tile.hover{background:linear-gradient(160deg,#2aa3b2,#1a8f9f);display:flex;flex-direction:column;align-items:center;justify-content:flex-start;padding-top:54px;color:var(--white);font-family:"Outfit",sans-serif;font-size:18.5px;line-height:23px;text-align:center}
.tile.hover .go{margin-top:16px;width:30px;height:30px;border:1.3px solid var(--white);border-radius:50%;display:flex;align-items:center;justify-content:center}

/* sectors */
.sector-photo{position:absolute;left:85px;top:2318px;width:611px;height:395px;background:linear-gradient(160deg,#c9a37a,#a8764a 50%,#7a5636)}
.sector-icon{position:absolute;left:93px;width:121px;height:121px;background:rgba(40,28,20,.62);display:flex;align-items:center;justify-content:center}
.sector-icon.on{background:var(--teal)}
.sector-card{position:absolute;left:584px;top:2400px;width:531px;height:232px;background:var(--white);border:1px solid #eee;padding:52px 34px 0 64px}
.sector-card h3{font-family:"Outfit",sans-serif;font-weight:400;font-size:28px;color:var(--ink)}
.sector-card h3 em{font-style:normal;color:var(--teal)}
.sector-card p{margin-top:14px;font-size:12px;line-height:16.8px;color:var(--grey)}

/* footer */
.footer-bg{position:absolute;left:0;top:2700px;width:1200px;height:576px}
.foot-h{position:absolute;left:350px;top:2935px;font-size:16.5px;font-weight:500;color:var(--white)}
.foot-call{position:absolute;left:350px;top:2969px;font-size:16.5px;font-weight:500;color:var(--teal)}
.foot-small{position:absolute;left:350px;font-size:11.6px;line-height:19px;color:#ddd}
.field{position:absolute;background:var(--field);border-radius:16px;font-size:10.5px;color:#888;padding:8px 16px}
.send{position:absolute;left:617px;top:3133px;width:97px;height:30px;border-radius:15px;background:var(--teal);color:var(--white);font-size:11px;font-weight:500;text-align:center;line-height:30px}
.copyright{position:absolute;left:0;top:3213px;width:1200px;text-align:center;font-size:12px;color:#ddd}
.copyright b{font-weight:400;color:var(--teal)}
</style>
</head>
<body>

<header class="site-header">
  <div class="brand">Tavrelo</div>
  <nav class="nav">
    <a class="active" style="left:378px">Home</a>
    <a style="left:449px">About Us</a>
    <a style="left:542px">Services</a>
    <a style="left:630px">Our Work</a>
    <a style="left:728px">Contact Us</a>
  </nav>
  <a class="social" style="left:844px;top:25px" aria-label="Social profile 1"></a>
  <a class="social on" style="left:883px;top:25px" aria-label="Social profile 2"></a>
  <a class="social" style="left:922px;top:25px" aria-label="Social profile 3"></a>
  <a class="pill solid" style="left:986px;top:25px;width:129px;height:31px;line-height:31px">GET IN TOUCH</a>
</header>

<section class="hero">
  <div class="hero-photo" role="img" aria-label="Team meeting around a table in a glass-walled office with red pendant lamps"></div>
  <h1 class="hero-title">Work Well Together</h1>
  <p class="hero-sub">Improving Your Collaboration Ecosystem To Create<br>A Better Tomorrow</p>
  <a class="hero-btn">CONTACT US</a>
  <span class="dot" style="top:266px"></span>
  <span class="dot on" style="top:285px"></span>
  <span class="dot" style="top:304px"></span>
  <span class="dot" style="top:323px"></span>
  <svg class="abs" style="left:0;top:515px" width="1200" height="170" viewBox="0 0 1200 170" aria-hidden="true">
    <path d="M0 90 C120 10 260 20 420 40 C650 70 900 110 1200 167 L1200 170 L0 170 Z" fill="#fff"/>
    <path d="M0 90 C120 10 260 20 420 40 C600 65 780 95 940 118 C780 80 620 55 420 32 C250 14 110 8 0 85 Z" fill="var(--teal)"/>
  </svg>
</section>

<section class="services">
  <div class="eyebrow" style="top:642px"><span>WHAT WE DO</span></div>
  <h2 class="heading section-title" style="top:654px">Services We Provide</h2>

  <div class="service fiber" role="img" aria-label="Blue network cabling in a patch panel">FIBER OPTIC<br>INSTALLATION</div>
  <div class="service av">
    <div class="frame"></div>
    <svg width="58" height="50" viewBox="0 0 58 50" aria-hidden="true">
      <path d="M2 17h11L28 4v42L13 33H2z" fill="#fff"/>
      <path d="M36 14c5 6 5 16 0 22M43 8c9 9 9 25 0 34" stroke="#fff" stroke-width="4" fill="none" stroke-linecap="round"/>
    </svg>
    AUDIO VISUAL
  </div>
  <div class="service comms" role="img" aria-label="Video conference room with screens">COMMUNICATIONS<br>SYSTEMS</div>
  <div class="service security" role="img" aria-label="Security camera mounted on a wall">SECURITY SYSTEMS<br>INSTALLATION</div>
</section>

<section class="about">
  <div class="about-mark"><span class="sq"></span><span class="name">Tavrelo</span></div>
  <div class="eyebrow-left">WHO WE ARE</div>
  <h2 class="heading about-title">About Tavrelo</h2>
  <div class="about-text">
    <p>It is a long established fact that a reader will be distracted by the readable content of a page when looking at its layout. The point of using Lorem Ipsum is that it has a more-or-less normal distribution of letters, as opposed to using 'Content here, content here', making it look like readable English.</p>
    <p>Many desktop publishing packages and web page editors now use Lorem Ipsum as their default model text, and a search for 'lorem ipsum...</p>
  </div>
  <a class="pill outline" style="left:616px;top:1412px;width:145px;height:31px;line-height:28px">DISCOVER MORE</a>
</section>

<section class="projects">
  <div class="eyebrow" style="top:1559px"><span>PHOTO GALLERY</span></div>
  <h2 class="heading section-title" style="top:1580px">Our Projects</h2>

  <div class="tile" style="left:85px;top:1658px;background:linear-gradient(160deg,#9fc3de,#4d7fa8 60%,#d8e4ec)" role="img" aria-label="Modern glass office building interior"></div>
  <div class="tile hover" style="left:431px;top:1658px">
    There are many variations<br>Ipsum available
    <span class="go"><svg width="14" height="10" viewBox="0 0 14 10" aria-hidden="true"><path d="M1 5h11M8 1l4 4-4 4" stroke="#fff" stroke-width="1.4" fill="none"/></svg></span>
  </div>
  <div class="tile" style="left:777px;top:1658px;background:linear-gradient(160deg,#e8e8e8,#c9c9c9 60%,#9a9080)" role="img" aria-label="Empty conference room with U-shaped table"></div>
  <div class="tile" style="left:85px;top:1868px;background:linear-gradient(160deg,#42506a,#d7d9dc 55%,#f2f2f2)" role="img" aria-label="Business people on a video call"></div>
  <div class="tile" style="left:431px;top:1868px;background:linear-gradient(160deg,#d9d3a6,#bdb27c 55%,#6c5aa0)" role="img" aria-label="Classroom with wall-mounted display"></div>
  <div class="tile" style="left:777px;top:1868px;background:linear-gradient(160deg,#cfcfcf,#b7b4ae 55%,#e9e9e9)" role="img" aria-label="Security devices: camera, keypad and sensors"></div>

  <a class="pill outline" style="left:528px;top:2110px;width:144px;height:32px;line-height:29px">VIEW ALL WORK</a>
</section>

<section class="sectors">
  <div class="eyebrow" style="top:2220px"><span>INDUSTRY WE SERVE</span></div>
  <h2 class="heading section-title" style="top:2240px">Sector Segregation</h2>

  <div class="sector-photo" role="img" aria-label="University lecture hall with curved wooden desks"></div>
  <div class="sector-icon" style="top:2326px" aria-label="Medical">
    <svg width="52" height="56" viewBox="0 0 52 56" fill="none" stroke="#fff" stroke-width="4" stroke-linecap="round" aria-hidden="true">
      <path d="M6 4v16a12 12 0 0 0 24 0V4"/><path d="M18 32v8a10 10 0 0 0 20 0v-6"/><circle cx="38" cy="30" r="5"/>
    </svg>
  </div>
  <div class="sector-icon on" style="top:2456px" aria-label="Education">
    <svg width="64" height="46" viewBox="0 0 64 46" aria-hidden="true">
      <path d="M32 2 62 14 32 26 2 14z" fill="#fff"/><path d="M14 20v12c6 6 30 6 36 0V20L32 28z" fill="#fff"/><path d="M56 16v18" stroke="#fff" stroke-width="3"/><circle cx="56" cy="36" r="3" fill="#fff"/>
    </svg>
  </div>
  <div class="sector-icon" style="top:2583px" aria-label="Government">
    <svg width="56" height="50" viewBox="0 0 56 50" fill="#fff" aria-hidden="true">
      <path d="M28 2 54 14H2z"/><rect x="6" y="18" width="6" height="22"/><rect x="18" y="18" width="6" height="22"/><rect x="32" y="18" width="6" height="22"/><rect x="44" y="18" width="6" height="22"/><rect x="2" y="43" width="52" height="5"/>
    </svg>
  </div>
  <article class="sector-card">
    <h3><em>01</em> - EDUCATIONS</h3>
    <p>Lorem Ipsum is simply dummy text of the printing and typesetting industry. Lorem Ipsum has been the industry's standard dummy text ever since the 1500s, when an unknown printer took a galley of type and scrambled it to make a type specimen book.</p>
  </article>
</section>

<footer>
  <svg class="footer-bg" viewBox="0 0 1200 576" aria-hidden="true">
    <path d="M0 110 C150 190 420 180 700 125 C900 85 1080 40 1200 0 L1200 576 L0 576 Z" fill="#000"/>
    <path d="M0 110 C120 175 330 185 520 160 C300 172 120 160 0 100 Z" fill="var(--teal)"/>
  </svg>
  <div class="brand" style="top:2946px;font-size:46px">Tavrelo</div>

  <div class="foot-h">CONTACT US</div>
  <div class="foot-call">Call Us: (02)-555-0148</div>
  <div class="foot-small" style="top:2995px">e. info@tavrelo.com</div>
  <div class="foot-small" style="top:3038px">Tavrelo<br>48 Harbour Line Rd<br>Ultimo, NSW 2007</div>
  <a class="social" style="left:350px;top:3132px" aria-label="Social profile 1"></a>
  <a class="social on" style="left:389px;top:3132px" aria-label="Social profile 2"></a>
  <a class="social" style="left:428px;top:3132px" aria-label="Social profile 3"></a>

  <div class="field" style="left:616px;top:2938px;width:209px;height:32px">Name</div>
  <div class="field" style="left:842px;top:2938px;width:209px;height:32px">Email</div>
  <div class="field" style="left:616px;top:2988px;width:435px;height:30px">Service</div>
  <div class="field" style="left:616px;top:3036px;width:435px;height:79px">Message ...</div>
  <div class="send">SEND</div>

  <svg class="abs" style="left:1146px;top:2938px" width="26" height="28" viewBox="0 0 26 28" aria-label="Back to top">
    <path d="M13 3v22M4 12l9-9 9 9" stroke="var(--teal)" stroke-width="2.5" fill="none" stroke-linecap="round"/>
  </svg>

  <div class="copyright">© 2020 <b>Tavrelo.</b> All Right Reserved</div>
</footer>

</body>
</html>
```